Flyer-Design für Hersteller von ökologischen Werbemitteln aus Papier/Karton
Zielgruppe
Wir machen ökologische Werbemittel aus Papier/Karton wie Parkscheiben, Drehscheiben usw.
Aufgabenstellung
Wir suchen den Content für einen Falzflyer im Format 220 x 150 mm (offen) bzw. 110 x 150 mm (geschlossen) mit folgenden Inhalten.
Seite 1: Frei/Leer
Seite 2 (Innen) : Speisekarte Pizzeria Valtoro Teil I (einfach ein paar Pizzen)
Seite 3 (Innen): Speiseikarte Pizzeria Valtoro Teil II (einfach ein paar Nudelgerichte)
Seite 4 (Rückseite): Zehn leere Felder für Stempel Pizzeria Valtoro (nach zehn Stempeln bekommt der Käufer eine Pizza gratis)
Das gesamte Design/Layout in einem Pizzierastyle.

```html
<!DOCTYPE html>
<html lang="de">
<head>
<meta charset="utf-8">
<title>Speisekarte Pizzeria Valtoro – Pizza, Pasta &amp; Salat</title>
<link rel="stylesheet" href="https://fonts.googleapis.com/css2?family=Open+Sans:ital,wght@0,400;0,700;1,400&family=Patrick+Hand+SC&display=swap">
<style>
  :root {
    --green: #41a935;
    --green-text: #3a9f31;
    --green-art-a: #4bb23e;
    --green-art-b: #389a2d;
    --paper: #ffffff;
  }
  * { margin: 0; padding: 0; box-sizing: border-box; }
  html, body { width: 1200px; height: 818px; overflow: hidden; background: var(--paper); }
  body { font-family: "Open Sans", Arial, sans-serif; color: var(--green-text); }
  .menu { position: relative; width: 1200px; height: 818px; }

  .band { position: absolute; top: 0; height: 88px; background: var(--green); overflow: hidden; }
  .band--pizza { left: 0; width: 599px; }
  .band--pasta { left: 601px; width: 599px; }
  .band__title {
    position: absolute; left: 39px; top: 22px;
    font-family: "Patrick Hand SC", "Comic Sans MS", cursive;
    font-size: 44px; letter-spacing: 2px; color: var(--paper); line-height: 1;
  }
  .band--pasta .band__title { left: 38px; }
  .band__art {
    position: absolute; top: 0; height: 88px;
    background: linear-gradient(90deg, var(--green-art-a), var(--green-art-b));
    opacity: .9;
  }
  .band--pizza .band__art { left: 300px; width: 299px; border-radius: 0 0 0 60px; }
  .band--pasta .band__art { left: 337px; width: 262px; border-radius: 0 0 0 50px; }

  .info { position: absolute; left: 39px; font-size: 17px; line-height: 22px; white-space: nowrap; }
  .info b { display: inline-block; width: 118px; font-weight: 700; }
  .note { position: absolute; left: 39px; top: 171px; font-size: 14.5px; }
  .diameter { position: absolute; left: 39px; top: 208px; width: 521px; font-size: 15px; }
  .diameter span { position: absolute; top: -2px; font-weight: 700; font-size: 17.5px; }

  .item { position: absolute; font-size: 17.5px; line-height: 21.5px; white-space: nowrap; }
  .item--pizza { left: 39px; width: 521px; }
  .item--pasta { left: 638px; width: 522px; }
  .item__num { position: absolute; left: 0; top: 0; }
  .item__desc { margin-left: 27px; }
  .item__desc b { font-weight: 700; }
  .item__desc i { font-style: italic; }
  .item__price { position: absolute; top: 0; font-weight: 700; }
  .item__price--small { right: 80px; }
  .item__price--large { right: 0; }
  .item--tall .item__desc { line-height: 27px; }
</style>
</head>
<body>
<main class="menu">
  <header class="band band--pizza">
    <div class="band__art" role="img" aria-label="Gezeichnete Pizza mit Tomaten, Basilikum und Oliven"></div>
    <h1 class="band__title">PIZZA</h1>
  </header>
  <header class="band band--pasta">
    <div class="band__art" role="img" aria-label="Gezeichnete Nudeln, Tomatenscheiben und Kräuter"></div>
    <h1 class="band__title">PASTA &amp; SALAT</h1>
  </header>

  <p class="info" style="top:112px"><b>PIZZABELAG</b>☛Alle Pizzen mit Tomatensoße und Käse</p>
  <p class="info" style="top:135px"><b>PIZZATEIG</b>☛Alle Pizzen mit Weizenmehl</p>
  <p class="note">Auf Bestellung (Aufpreis) auch mit 100%-igem Dinkel- oder glutenfreien Mehl.</p>
  <p class="diameter">Durchmesser:<span style="right:80px">Ø 25 cm</span><span style="right:0">Ø 31 cm</span></p>

  <section class="pizza-list">
    <div class="item item--pizza" style="top:244px"><span class="item__num">01</span><p class="item__desc"><b>MARGHERITA</b> <i>mit Tomaten und Mozzarella</i></p><span class="item__price item__price--small">5,00 €</span><span class="item__price item__price--large">6,00 €</span></div>
    <div class="item item--pizza" style="top:271px"><span class="item__num">02</span><p class="item__desc"><b>FUNGHI</b> <i>mit frischen Champignons</i></p><span class="item__price item__price--small">5,50 €</span><span class="item__price item__price--large">6,50 €</span></div>
    <div class="item item--pizza" style="top:298px"><span class="item__num">03</span><p class="item__desc"><b>SALAME</b> <i>mit Salami</i></p><span class="item__price item__price--small">5,50 €</span><span class="item__price item__price--large">6,50 €</span></div>
    <div class="item item--pizza" style="top:324px"><span class="item__num">04</span><p class="item__desc"><b>DIAVOLO</b> <i>mit Salami, Peperoni - scharf</i></p><span class="item__price item__price--small">5,50 €</span><span class="item__price item__price--large">6,50 €</span></div>
    <div class="item item--pizza" style="top:351px"><span class="item__num">05</span><p class="item__desc"><b>PROSCIUTTO</b> <i>mit Vorderschinken</i></p><span class="item__price item__price--small">5,50 €</span><span class="item__price item__price--large">6,50 €</span></div>
    <div class="item item--pizza" style="top:379px"><span class="item__num">06</span><p class="item__desc"><b>CALABRIA</b> <i>mit Salami und Champignons</i></p><span class="item__price item__price--small">7,50 €</span><span class="item__price item__price--large">8,50 €</span></div>
    <div class="item item--pizza" style="top:406px"><span class="item__num">07</span><p class="item__desc"><b>AMORE</b> <i>mit Vorderschinken und Champignons</i></p><span class="item__price item__price--small">7,50 €</span><span class="item__price item__price--large">8,50 €</span></div>
    <div class="item item--pizza" style="top:433px"><span class="item__num">08</span><p class="item__desc"><b>HAWAII</b> <i>mit Vorderschinken und Ananas</i></p><span class="item__price item__price--small">7,50 €</span><span class="item__price item__price--large">8,50 €</span></div>
    <div class="item item--pizza" style="top:459px"><span class="item__num">09</span><p class="item__desc"><b>SICILIANA</b> <i>mit Mozzarella, Kapern, Oliven,</i></p><span class="item__price item__price--small">10,50 €</span><span class="item__price item__price--large">11,50 €</span></div>
    <div class="item item--pizza item--tall" style="top:483px"><span class="item__num" style="top:3px">14</span><p class="item__desc"><b>QUATTRO STAGIONI</b> <i>mit Vorderschinken,</i><br><i>Salami, frischen Champignons, Paprika</i></p><span class="item__price item__price--small" style="top:3px">10,50 €</span><span class="item__price item__price--large" style="top:3px">11,50 €</span></div>
    <div class="item item--pizza" style="top:541px"><span class="item__num">10</span><p class="item__desc"><b>RUCOLA</b> <i>mit Rucola, Cherrytomaten und</i><br><i>Parmesan</i></p><span class="item__price item__price--small">7,50 €</span><span class="item__price item__price--large">8,50 €</span></div>
    <div class="item item--pizza" style="top:589px"><span class="item__num">11</span><p class="item__desc"><b>SARDELLE</b> <i>mit Sardellen</i></p><span class="item__price item__price--small">6,50 €</span><span class="item__price item__price--large">7,50 €</span></div>
    <div class="item item--pizza" style="top:616px"><span class="item__num">12</span><p class="item__desc"><b>TONNO</b> <i>mit Thunfisch und Zwiebeln</i></p><span class="item__price item__price--small">7,50 €</span><span class="item__price item__price--large">8,50 €</span></div>
    <div class="item item--pizza" style="top:642px"><span class="item__num">13</span><p class="item__desc"><b>SALMONE</b> <i>mit Lachs, Spinat und Mozzarella</i></p><span class="item__price item__price--small">9,50 €</span><span class="item__price item__price--large">10,50 €</span></div>
    <div class="item item--pizza" style="top:669px"><span class="item__num">15</span><p class="item__desc"><b>FORMAGGI</b><br><i>mit 4 verschiedenen Käsesorten</i></p><span class="item__price item__price--small">8,50 €</span><span class="item__price item__price--large">9,50 €</span></div>
    <div class="item item--pizza" style="top:717px"><span class="item__num">16</span><p class="item__desc"><b>PIZZA BRÖTCHEN</b> <i>mit Käse</i></p><span class="item__price item__price--small">6 Stück</span><span class="item__price item__price--large">5,90 €</span></div>
    <div class="item item--pizza" style="top:744px"><span class="item__num">17</span><p class="item__desc"><b>PIZZA BRÖTCHEN</b> <i>mit Knoblauch</i></p><span class="item__price item__price--small">6 Stück</span><span class="item__price item__price--large">5,90 €</span></div>
  </section>

  <section class="pasta-list">
    <div class="item item--pasta" style="top:150px"><span class="item__num">18</span><p class="item__desc"><b>SPAGHETTI BOLOGNESE</b> <i>mit Hackfleischsoße</i></p><span class="item__price item__price--large">7,50 €</span></div>
    <div class="item item--pasta" style="top:177px"><span class="item__num">19</span><p class="item__desc"><b>RIGATONI AL FORNO</b> <i>mit Hackfleischsoße</i><br><i>und Schinken, mit Käse überbacken</i></p><span class="item__price item__price--large">8,00 €</span></div>
    <div class="item item--pasta" style="top:225px"><span class="item__num">20</span><p class="item__desc"><b>CANNELLONI CON SPINACI</b> <i>mit Spinatfüllung</i><br><i>in Sahnesoße, mit Käse überbacken</i></p><span class="item__price item__price--large">8,50 €</span></div>
    <div class="item item--pasta" style="top:273px"><span class="item__num">21</span><p class="item__desc"><b>LASAGNA</b> <i>Nudelauflauf mit Hackfleischsoße,</i><br><i>mit Käse überbacken</i></p><span class="item__price item__price--large">8,50 €</span></div>
    <div class="item item--pasta" style="top:321px"><span class="item__num">22</span><p class="item__desc"><b>CANNELLONI</b> <i>mit Fleischfüllung, mit Käse überbacken</i></p><span class="item__price item__price--large">9,50 €</span></div>
    <div class="item item--pasta" style="top:348px"><span class="item__num">23</span><p class="item__desc"><b>SPAGHETTI AGLIO E OLIO</b> <i>mit Knoblauch</i></p><span class="item__price item__price--large">7,50 €</span></div>
    <div class="item item--pasta" style="top:374px"><span class="item__num">24</span><p class="item__desc"><b>SPAGHETTI CON SCAMPI</b> <i>mit Knoblauch und Scampi</i></p><span class="item__price item__price--large">11,50 €</span></div>
    <div class="item item--pasta" style="top:401px"><span class="item__num">25</span><p class="item__desc"><b>TAGLIATELLE CARBONARA</b> <i>mit Vorderschinken</i><br><i>in Sahnesoße</i></p><span class="item__price item__price--large">10,50 €</span></div>
    <div class="item item--pasta" style="top:449px"><span class="item__num">26</span><p class="item__desc"><b>TAGLIATELLE AL SALMONE</b> <i>mit Lachs in Sahnesoße</i></p><span class="item__price item__price--large">11,50 €</span></div>

    <div class="item item--pasta" style="top:530px"><span class="item__num">27</span><p class="item__desc"><b>INSALATA MISTA</b> <i>gemischter Salat, Tomaten, Gurken</i><br><i>und French-Dressing</i></p><span class="item__price item__price--large">4,50 €</span></div>
    <div class="item item--pasta" style="top:578px"><span class="item__num">28</span><p class="item__desc"><b>INSALATA DI RUCOLA</b> <i>mit Cherrytomaten, Parmesan</i><br><i>und Balsamico-Dressing</i></p><span class="item__price item__price--large">5,50 €</span></div>
    <div class="item item--pasta" style="top:627px"><span class="item__num">29</span><p class="item__desc"><b>INSALATA SPECIALE</b> <i>gemischter Salat mit Vorder-</i><br><i>schinken, Käse und Ei</i></p><span class="item__price item__price--large">7,50 €</span></div>
    <div class="item item--pasta" style="top:675px"><span class="item__num">30</span><p class="item__desc"><b>INSALATA ITALIA</b> <i>gemischter Salat mit Thunfisch,</i><br><i>Artischocken, Käse und Ei</i></p><span class="item__price item__price--large">9,50 €</span></div>
    <div class="item item--pasta" style="top:724px"><span class="item__num">31</span><p class="item__desc"><b>INSALATA MARE</b> <i>gemischter Salat mit Meeresfrüchten,</i><br><i>Thunfisch und Zwiebeln</i></p><span class="item__price item__price--large">10,50 €</span></div>
  </section>
</main>
</body>
</html>
```